Business card for STEADYWAVE

Please design professional business card for IT consulting firm STEADYWAVE INC.
Use logo attached.
Use information from sample qNode business card attached.
replace qnode inc with STEADYWAVE INC.
as well as qnodeinc.com with steadywave.example

```html
<!DOCTYPE html>
<html lang="en">
<head>
<meta charset="utf-8">
<title>STEADYWAVE business card</title>
<link href="https://fonts.googleapis.com/css2?family=Lato:wght@400;700;900&display=swap" rel="stylesheet">
<style>
  :root {
    --backdrop: #e9e6e2;
    --card-dark: #050505;
    --card-light: #f7f7f7;
    --ink: #111111;
    --ink-soft: #2a2a2a;
    --white: #ffffff;
    --map-tone: #2b2b2b;
    --spectrum: linear-gradient(90deg, #6a3aa8 0%, #3f7fe0 30%, #35c3e0 55%, #4fd3a8 75%, #e8b53a 100%);
    --spectrum-vertical: linear-gradient(0deg, #6a3aa8 0%, #3f7fe0 30%, #35c3e0 55%, #6fd27a 80%, #d8d23a 100%);
  }
  * { box-sizing: border-box; margin: 0; padding: 0; }
  html, body { width: 1200px; height: 960px; overflow: hidden; }
  body {
    background: var(--backdrop);
    font-family: "Lato", sans-serif;
    color: var(--ink);
    position: relative;
  }
  .card {
    position: absolute;
    left: 250px;
    width: 700px;
    height: 400px;
    overflow: hidden;
    box-shadow: 0 6px 18px rgba(0,0,0,0.12);
  }
  /* Front side */
  .card-front { top: 50px; background: var(--card-dark); }
  .world-map {
    position: absolute;
    left: 60px; top: 40px;
    width: 600px; height: 300px;
    background: radial-gradient(ellipse at 50% 45%, var(--map-tone) 0%, rgba(43,43,43,0.55) 45%, rgba(5,5,5,0) 72%);
  }
  .front-logo {
    position: absolute;
    left: 180px; top: 168px;
    display: flex; align-items: center; gap: 14px;
  }
  .logo-word {
    font-weight: 700;
    letter-spacing: 0.2em;
    line-height: 1;
  }
  .front-logo .logo-word { font-size: 48px; color: var(--white); }
  .logo-square { width: 18px; height: 18px; background: var(--white); }
  .front-band {
    position: absolute; left: 0; right: 0; bottom: 0;
    height: 14px;
    background: var(--spectrum);
  }
  /* Back side */
  .card-back { top: 510px; background: var(--card-light); }
  .back-band {
    position: absolute; left: 0; top: 0; bottom: 0;
    width: 16px;
    background: var(--spectrum-vertical);
  }
  .back-content { position: absolute; left: 58px; top: 44px; right: 40px; }
  .back-logo { display: flex; align-items: center; gap: 12px; margin-bottom: 14px; }
  .back-logo .logo-word { font-size: 46px; color: var(--ink); }
  .back-logo .logo-square { background: var(--ink); width: 16px; height: 16px; }
  .person { display: flex; gap: 30px; font-size: 15px; line-height: 1.35; color: var(--ink-soft); }
  .person-name { font-size: 20px; font-weight: 900; color: var(--ink); }
  .person-name .credential { font-size: 14px; font-weight: 700; }
  .person-title { text-transform: uppercase; letter-spacing: 0.02em; }
  .label { font-weight: 700; color: var(--ink); }
  .person-extra { padding-top: 27px; }
  .offices { display: flex; margin-top: 16px; font-size: 15px; line-height: 1.35; color: var(--ink-soft); }
  .office { padding-right: 22px; }
  .office + .office { border-left: 1.5px solid var(--ink); padding-left: 22px; }
  .office-heading { font-weight: 700; color: var(--ink); }
</style>
</head>
<body>
  <section class="card card-front">
    <div class="world-map" role="img" aria-label="Dotted world map in dark grey"></div>
    <div class="front-logo">
      <span class="logo-word">STEADYWAVE</span>
      <span class="logo-square"></span>
    </div>
    <div class="front-band"></div>
  </section>

  <section class="card card-back">
    <div class="back-band"></div>
    <div class="back-content">
      <div class="back-logo">
        <span class="logo-word">STEADYWAVE</span>
        <span class="logo-square"></span>
      </div>
      <div class="person">
        <div class="person-main">
          <div class="person-name">DARIEN VOLKOVSKY, <span class="credential">P.ENG.</span></div>
          <div class="person-title">General Manager</div>
          <div><span class="label">o.</span> (555) 201-3340 ext.201</div>
          <div><span class="label">e.</span> dvolkovsky@steadywave.example</div>
        </div>
        <div class="person-extra">
          <div><span class="label">c.</span> (555) 418-2290</div>
          <div>www.steadywave.example</div>
        </div>
      </div>
      <div class="offices">
        <div class="office">
          <div class="office-heading">STEADYWAVE INC.</div>
          <div class="office-heading">Headquarters</div>
          <div>1280 Harlow Court, Suite 101</div>
          <div>Riverton, Ontario, L0A 1B2</div>
          <div>Canada</div>
          <div><span class="label">p.</span> (555) 614-7720</div>
        </div>
        <div class="office">
          <div class="office-heading">Coastal Office</div>
          <div>72 Cedarline Rd, Port Elms</div>
          <div>British Columbia, V0X 3K9</div>
          <div>Canada</div>
          <div><span class="label">p.</span> (555) 930-5518</div>
        </div>
      </div>
    </div>
  </section>
</body>
</html>
```